" Cavalto Solutions oferece serviços de automação de tarefas manuais repetitivas realizadas na administração das empresas, como ingresso de faturas, coleta de dados de vários sistemas e consolidação manual, aceso a site para extração de dados e posterior registro em sistemas próprios, etc. Os serviços que oferece são: a identificação dessas oportunidades apoiando no budiness case, o desenvolvimento dos robôs para automação, a implantação do modelo de governança para assegurar a boa implantação e posterior sustentabilidade, transferência de conhecimento para as equipes internos, e finalmente o suporte e manutenção da plataforma. "

```html
<!DOCTYPE html>
<html lang="pt-BR">
<head>
<meta charset="UTF-8">
<title>Cavalto Solutions – RPA</title>
<link href="https://fonts.googleapis.com/css2?family=Open+Sans:wght@400;600;700&display=swap" rel="stylesheet">
<style>
  :root {
    --cyan: #1fb3d4;
    --cyan-deep: #1583b8;
    --navy: #1e3350;
    --text: #5a5f66;
    --muted: #9aa0a6;
    --line: #e4e7ea;
    --page: #ffffff;
    --strip: #f5f6f7;
  }
  * { box-sizing: border-box; margin: 0; padding: 0; }
  html, body { width: 1200px; height: 1200px; overflow: hidden; }
  body {
    font-family: "Open Sans", sans-serif;
    background: var(--page);
    color: var(--text);
    display: flex; flex-direction: column;
  }
  .topbar {
    flex: none;
    height: 44px;
    background: linear-gradient(90deg, var(--cyan-deep), var(--cyan));
    display: flex; align-items: center; justify-content: flex-end;
    padding: 0 70px;
    color: #fff; font-size: 15px; gap: 10px;
  }
  .topbar svg { width: 16px; height: 16px; }
  .header {
    flex: none;
    height: 120px;
    display: flex; align-items: center; justify-content: space-between;
    padding: 0 70px;
    border-bottom: 1px solid var(--line);
  }
  .brand { display: flex; align-items: center; gap: 14px; }
  .brand-mark { width: 34px; height: 34px; background: var(--cyan); }
  .brand-name {
    font-size: 30px; font-weight: 700; color: var(--navy);
    letter-spacing: 1px; text-transform: uppercase;
  }
  .nav { display: flex; gap: 38px; font-size: 17px; color: var(--navy); font-weight: 600; }
  .nav .active { color: var(--cyan); }
  .page-title {
    flex: none;
    height: 96px; background: var(--strip);
    padding: 20px 70px;
    border-bottom: 1px solid var(--line);
  }
  .page-title h1 { font-size: 24px; color: var(--navy); font-weight: 700; }
  .breadcrumb { font-size: 13px; color: var(--muted); margin-top: 4px; }
  .intro {
    flex: none;
    display: flex; gap: 50px;
    padding: 44px 70px 0;
  }
  .intro-text { flex: 1; }
  .intro-text h2 {
    font-size: 31px; line-height: 1.25; color: var(--navy);
    font-weight: 700; text-transform: uppercase; margin-bottom: 24px;
  }
  .intro-text p { font-size: 17px; line-height: 1.6; margin-bottom: 18px; }
  .intro-visual {
    width: 500px; height: 390px;
    background: linear-gradient(160deg, #2f7fd0, #1a5fb8);
  }
  .benefits {
    flex: 1;
    display: flex; flex-direction: column;
    margin-top: 40px;
  }
  .benefits-title {
    text-align: center;
    font-size: 28px; font-weight: 600; color: var(--cyan-deep);
    text-transform: uppercase;
  }
  .benefits-title::after {
    content: ""; display: block; width: 70px; height: 3px;
    background: var(--cyan); margin: 12px auto 0;
  }
  .benefits-band {
    flex: 1;
    margin-top: 26px;
    background:
      radial-gradient(ellipse at 80% 20%, rgba(255,255,255,0.18), transparent 55%),
      linear-gradient(90deg, var(--cyan-deep), var(--cyan));
    display: flex; align-items: center; justify-content: center;
  }
  .benefit-icon {
    width: 96px; height: 96px;
    border: 3px solid rgba(255,255,255,0.85);
    border-radius: 50%;
  }
</style>
</head>
<body>
  <div class="topbar">
    <svg viewBox="0 0 24 24" fill="#fff"><path d="M6.6 10.8a15 15 0 0 0 6.6 6.6l2.2-2.2a1 1 0 0 1 1-.25 11.4 11.4 0 0 0 3.6.57 1 1 0 0 1 1 1V20a1 1 0 0 1-1 1A17 17 0 0 1 3 4a1 1 0 0 1 1-1h3.5a1 1 0 0 1 1 1c0 1.25.2 2.45.57 3.57a1 1 0 0 1-.25 1z"/></svg>
    <span>(11) 3000-4500</span>
  </div>

  <header class="header">
    <div class="brand">
      <span class="brand-mark"></span>
      <span class="brand-name">Cavalto Solutions</span>
    </div>
    <nav class="nav">
      <span class="active">Home</span>
      <span>Quem Somos</span>
      <span>RPA</span>
      <span>Serviços ▾</span>
      <span>Contato</span>
    </nav>
  </header>

  <section class="page-title">
    <h1>RPA</h1>
    <div class="breadcrumb">Home / RPA</div>
  </section>

  <section class="intro">
    <div class="intro-text">
      <h2>O que é RPA? Robotic Process Automation</h2>
      <p>É uma solução de automação de processos/tarefas manuais e repetitivas por meio de software.</p>
      <p>Tarefas que são realizadas atualmente por usuários de sistemas, podendo ser realizadas diretamente pelo software (robô). Como exemplo claro, a marcação entre vários sistemas, planilhas e envios de resultados por e-mail. Outro exemplo é a coleta de dados de vários sistemas, sites, planilhas e consolidação dos resultados em uma base.</p>
    </div>
    <div class="intro-visual" role="img" aria-label="Ilustração de mão robótica cercada de ícones de tecnologia sobre fundo azul"></div>
  </section>

  <section class="benefits">
    <h3 class="benefits-title">Benefícios de RPA</h3>
    <div class="benefits-band" role="img" aria-label="Faixa azul com ícones ilustrando os benefícios da automação">
      <span class="benefit-icon"></span>
    </div>
  </section>
</body>
</html>
```